Brelora
business card, seafood selling company
Professional
Kaloyan Terziev
Manager
14A, Vasil Mirkov str,
Sofia, Bulgaria,
postal code: 1486
k.terziev@brelora-demo.bg
www.brelora-demo.bg
I want a good looking and stylish business card.
I didn't decide it yet. I hope I will receive good and fresh ideas.
Here is our logo which have to be used in the business card

```html
<!DOCTYPE html>
<html lang="en">
<head>
<meta charset="utf-8">
<title>Brelora – business card set</title>
<link href="https://fonts.googleapis.com/css2?family=Open+Sans:wght@400;600;800&display=swap" rel="stylesheet">
<style>
  :root {
    --navy: #1d2a78;
    --navy-deep: #141d5a;
    --blue: #2e44a8;
    --orange: #f05a2b;
    --orange-light: #f57a45;
    --paper: #ffffff;
    --paper-shade: #e9ecf2;
    --ink-grey: #6b6f7a;
    --stage: #ececec;
  }
  * { margin: 0; padding: 0; box-sizing: border-box; }
  html, body { width: 1200px; height: 770px; overflow: hidden; }
  body {
    background: var(--stage);
    font-family: "Open Sans", Arial, sans-serif;
    position: relative;
  }
  .card {
    position: absolute;
    border-radius: 16px;
    overflow: hidden;
    box-shadow: 0 4px 10px rgba(0,0,0,0.18);
  }
  .card svg.waves { position: absolute; inset: 0; width: 100%; height: 100%; }
  .card-contact { left: 100px; top: 96px; width: 500px; height: 288px; background: linear-gradient(180deg, var(--paper), var(--paper-shade)); }
  .card-orange { left: 629px; top: 96px; width: 432px; height: 288px; background: linear-gradient(135deg, var(--orange-light), var(--orange)); }
  .card-navy { left: 100px; top: 403px; width: 500px; height: 293px; background: linear-gradient(160deg, var(--blue), var(--navy-deep)); }
  .card-logo { left: 629px; top: 403px; width: 432px; height: 293px; background: var(--paper); }

  .brand { position: absolute; display: flex; flex-direction: column; align-items: flex-start; }
  .brand-row { display: flex; align-items: center; gap: 8px; }
  .brand-dot { width: 12px; height: 12px; border-radius: 50%; background: var(--orange); }
  .brand-name { font-weight: 800; font-size: 34px; line-height: 1; letter-spacing: 1px; color: var(--navy); }
  .brand-tagline { font-size: 9px; font-weight: 600; letter-spacing: 1px; color: var(--navy); margin-top: 4px; margin-left: 20px; }
  .brand.on-dark .brand-name, .brand.on-dark .brand-tagline { color: #fff; }
  .brand.on-dark .brand-dot { background: #fff; }

  .card-contact .brand { left: 40px; top: 32px; }
  .card-contact .brand-name { font-size: 30px; }
  .card-orange .brand { left: 50%; top: 50%; transform: translate(-50%, -50%); }
  .card-navy .brand { left: 150px; top: 48px; }
  .card-logo .brand { left: 50%; top: 44%; transform: translate(-50%, -50%); }
  .card-logo .brand-name { font-size: 40px; }
  .card-logo .brand-tagline { font-size: 11px; color: var(--blue); }

  .person { position: absolute; left: 305px; top: 100px; }
  .person-name { font-size: 17px; font-weight: 600; color: var(--orange); }
  .person-role { font-size: 12px; color: var(--ink-grey); margin-top: 2px; }

  .address { position: absolute; left: 28px; top: 118px; font-size: 10px; line-height: 14px; color: var(--ink-grey); }
  .contacts { position: absolute; left: 28px; top: 172px; list-style: none; font-size: 9.5px; line-height: 14px; color: var(--ink-grey); }
  .contacts li { display: flex; align-items: center; gap: 6px; }
  .contacts svg { width: 9px; height: 9px; flex: none; }
</style>
</head>
<body>

<section class="card card-contact">
  <svg class="waves" viewBox="0 0 500 288" preserveAspectRatio="none" aria-hidden="true">
    <path d="M0,0 L170,0 C110,8 50,30 0,70 Z" fill="var(--navy)"/>
    <path d="M0,78 C50,36 120,12 200,4" fill="none" stroke="var(--orange)" stroke-width="4"/>
    <path d="M0,262 C140,290 300,150 500,140 L500,288 L0,288 Z" fill="var(--navy)"/>
    <path d="M0,250 C140,278 300,138 500,128" fill="none" stroke="var(--orange)" stroke-width="5"/>
  </svg>
  <div class="brand">
    <div class="brand-row"><span class="brand-dot"></span><span class="brand-name">BRELORA</span></div>
    <span class="brand-tagline">HIGH QUALITY PRODUCTS</span>
  </div>
  <div class="person">
    <p class="person-name">Kaloyan Terziev</p>
    <p class="person-role">Manager</p>
  </div>
  <p class="address">14A, Vasil Mirkov str,<br>Sofia, Bulgaria,<br>postal code: 1486</p>
  <ul class="contacts">
    <li><svg viewBox="0 0 10 10"><rect width="10" height="10" fill="var(--orange)"/></svg>+359 888 40 27 15</li>
    <li><svg viewBox="0 0 10 10"><rect width="10" height="10" fill="var(--orange)"/></svg>+359 2 971 36 08</li>
    <li><svg viewBox="0 0 10 10"><rect width="10" height="10" fill="var(--orange)"/></svg>k.terziev@brelora-demo.bg</li>
    <li><svg viewBox="0 0 10 10"><rect width="10" height="10" fill="var(--orange)"/></svg>www.brelora-demo.bg</li>
  </ul>
</section>

<section class="card card-orange">
  <div class="brand on-dark">
    <div class="brand-row"><span class="brand-dot"></span><span class="brand-name">BRELORA</span></div>
    <span class="brand-tagline">HIGH QUALITY PRODUCTS</span>
  </div>
</section>

<section class="card card-navy">
  <svg class="waves" viewBox="0 0 500 293" preserveAspectRatio="none" aria-hidden="true">
    <path d="M0,250 C150,285 320,190 500,170" fill="none" stroke="rgba(255,255,255,0.25)" stroke-width="3"/>
  </svg>
  <div class="brand on-dark">
    <div class="brand-row"><span class="brand-dot"></span><span class="brand-name">BRELORA</span></div>
    <span class="brand-tagline">HIGH QUALITY PRODUCTS</span>
  </div>
</section>

<section class="card card-logo">
  <svg class="waves" viewBox="0 0 432 293" preserveAspectRatio="none" aria-hidden="true">
    <path d="M250,0 C320,20 380,50 432,95 L432,0 Z" fill="var(--orange)"/>
    <path d="M200,0 C300,18 380,55 432,110" fill="none" stroke="var(--navy)" stroke-width="3"/>
    <path d="M0,235 C120,290 280,190 432,205 L432,293 L0,293 Z" fill="var(--navy)"/>
    <path d="M0,224 C120,278 280,178 432,193" fill="none" stroke="var(--orange)" stroke-width="5"/>
  </svg>
  <div class="brand">
    <div class="brand-row"><span class="brand-dot"></span><span class="brand-name">BRELORA</span></div>
    <span class="brand-tagline">HIGH QUALITY PRODUCTS</span>
  </div>
</section>

</body>
</html>
```